Criação de Power Point Slide Mestre para Rocha & Vento
" A Lunavix atua como desenvolvedora e estruturadora de soluções energéticas. É responsável pela prospecção de clientes, análise técnica e regulatória, validação de faturas, estruturação do modelo econômico e coordenação do pré-projeto. A implantação, financiamento, tecnologia e operação dos sistemas são executados por parceiros estratégicos especializados, sob um modelo de longo prazo baseado em disponibilidade, performance e economia para o cliente final. "

```html
<!DOCTYPE html>
<html lang="pt-BR">
<head>
<meta charset="utf-8">
<title>Lunavix — Slide Mestre</title>
<link rel="stylesheet" href="https://fonts.googleapis.com/css2?family=Montserrat:wght@400;500;600;700;800&display=swap">
<style>
  :root {
    --stage: #a6a6a6;
    --paper: #ffffff;
    --navy: #1d3768;
    --blue: #1f4aa0;
    --sky: #4aa3df;
    --yellow: #f5b417;
    --text: #3c4350;
    --muted: #7a808a;
    --rule: #c9ccd2;
  }
  * { margin: 0; padding: 0; box-sizing: border-box; }
  html, body {
    width: 1200px; height: 1200px; overflow: hidden;
    background: var(--stage);
    font-family: "Montserrat", sans-serif;
  }
  .slide {
    position: absolute; left: 24px; top: 276px;
    width: 1152px; height: 648px;
    background: var(--paper); overflow: hidden;
  }
  .decor { position: absolute; left: 0; top: 0; }
  .person {
    position: absolute; left: 48px; top: 96px; width: 300px; height: 552px;
    border-radius: 150px 150px 0 0;
    background: linear-gradient(180deg, #d9b98d 0%, #c9972f 45%, #b8892c 75%, #9fb0c4 100%);
  }
  .brand {
    position: absolute; left: 78px; top: 30px;
    display: flex; align-items: center; gap: 8px;
    font-weight: 700; font-size: 22px; color: var(--sky);
  }
  .brand-dot { width: 16px; height: 16px; border-radius: 50%; background: var(--yellow); }
  .title {
    position: absolute; left: 487px; top: 48px;
    font-weight: 800; font-size: 35px; line-height: 43px; color: var(--navy);
  }
  .title .accent { color: var(--yellow); }
  .block { position: absolute; left: 497px; display: flex; gap: 20px; }
  .block--checks { top: 208px; }
  .block--permits { top: 380px; }
  .icon-box {
    width: 79px; height: 153px; border-radius: 6px;
    display: flex; align-items: center; justify-content: center; flex-shrink: 0;
  }
  .icon-box--blue { background: var(--blue); }
  .icon-box--yellow { background: var(--yellow); }
  .block h2 { font-size: 18px; font-weight: 700; color: var(--navy); margin: 4px 0 6px; }
  .block ul { list-style: none; }
  .block li { font-size: 12.5px; line-height: 17px; color: var(--text); }
  .block li::before { content: "- "; }
  .footer-rule {
    position: absolute; left: 487px; right: 48px; top: 605px;
    height: 1px; background: var(--rule);
  }
  .footer {
    position: absolute; left: 487px; right: 48px; top: 616px;
    display: flex; justify-content: space-between;
    font-size: 11px; letter-spacing: 3px; color: var(--muted);
  }
  .footer .page strong { color: var(--navy); font-weight: 700; }
</style>
</head>
<body>
  <div class="slide">
    <svg class="decor" width="480" height="648" viewBox="0 0 480 648" aria-hidden="true">
      <path d="M312 8 C300 120 330 230 410 330 C470 410 470 540 420 648 L250 648 L250 200 Z" fill="var(--sky)"/>
      <circle cx="216" cy="326" r="228" fill="var(--yellow)"/>
    </svg>
    <div class="person" role="img" aria-label="Fotografia de uma mulher sorridente de camisa mostarda segurando um tablet"></div>

    <div class="brand"><span class="brand-dot"></span>Lunavix</div>

    <h1 class="title">Verificação Técnica, Regulatória<br>e Econômica de Projetos para<br><span class="accent">Comercialização de Ativos</span></h1>

    <section class="block block--checks">
      <div class="icon-box icon-box--blue">
        <svg width="44" height="70" viewBox="0 0 44 70" fill="none" stroke="#fff" stroke-width="3" stroke-linecap="round">
          <circle cx="22" cy="16" r="11"/>
          <path d="M22 27 V44 M14 44 H30 V54 H14 Z M18 44 V38 M26 44 V38 M22 54 V66"/>
        </svg>
      </div>
      <div>
        <h2>Comprovamos os pontos básicos a considerar:</h2>
        <ul>
          <li>Localização do ativo/projeto;</li>
          <li>Regularização fundiária;</li>
          <li>Arrendamento configurado para um Direito de Superfície;</li>
          <li>Recurso renovável e as capacidades do projeto;</li>
          <li>Tecnologias aplicadas e equipamentos;</li>
          <li>Histórico e desempenho do projeto.</li>
        </ul>
      </div>
    </section>

    <section class="block block--permits">
      <div class="icon-box icon-box--yellow">
        <svg width="48" height="48" viewBox="0 0 48 48" fill="none" stroke="#fff" stroke-width="3" stroke-linecap="round">
          <circle cx="24" cy="24" r="20"/>
          <path d="M26 12 L18 26 H26 L22 36"/>
        </svg>
      </div>
      <div>
        <h2>Autorizações essenciais do tipo:</h2>
        <ul>
          <li>Outorgas e Concessões Parecer de Acesso;</li>
          <li>Licenças ambientais;</li>
          <li>Autorização de Supressão Vegetal;</li>
          <li>Alvará de Construção;</li>
          <li>Analisamos os acordos PPA's;</li>
          <li>Financiamento estruturado;</li>
          <li>Estudos de custos do O&amp;M.</li>
        </ul>
      </div>
    </section>

    <div class="footer-rule"></div>
    <div class="footer">
      <span>WWW.LUNAVIX.COM</span>
      <span class="page">PÁGINA <strong>07</strong></span>
    </div>
  </div>
</body>
</html>
```